Valbrook Data Works

Our company is about IT hardwares and IT solutions. IT hardware such as PC, RAMS, storage and servers. IT solutions such as project management, BA. We are also selling new technology too.

Target Market(s)

Consumer, Small to Medium Business, Corporate

Requirements
Must have
• The business card must have the following:
• Name:
• Title:
• Contact Number:
• Email address:
• Website:
• Color: Must match the logo color upgrade

```html
<!DOCTYPE html>
<html lang="en">
<head>
<meta charset="utf-8">
<title>Valbrook Data Works – Business Card</title>
<link rel="stylesheet" href="https://fonts.googleapis.com/css2?family=Michroma&family=Saira:wght@400;700&display=swap">
<style>
  :root {
    --bg: #d9d9d9;
    --paper: #f7f7f7;
    --charcoal: #4a4a4a;
    --charcoal-dark: #3d3d3d;
    --orange: #d98a2b;
    --orange-deep: #c8732f;
    --ink: #4d4d4d;
    --white: #ffffff;
  }
  * { box-sizing: border-box; margin: 0; padding: 0; }
  html, body { width: 1200px; height: 864px; overflow: hidden; }
  body { background: var(--bg); position: relative; font-family: "Saira", sans-serif; }

  .card {
    position: absolute;
    width: 560px;
    height: 320px;
    overflow: hidden;
    box-shadow: 0 14px 30px rgba(0,0,0,0.18);
  }
  .card-back { left: 580px; top: 90px; background: var(--paper); }
  .card-front { left: 60px; top: 460px; background: var(--charcoal); }

  .card-bg { position: absolute; inset: 0; }

  .back-band { position: absolute; left: 0; top: 0; width: 58px; height: 100%; background: var(--orange); }
  .back-rule { position: absolute; left: 64px; top: 0; width: 3px; height: 100%; background: var(--charcoal-dark); }

  .brand {
    position: absolute;
    display: flex;
    align-items: center;
    gap: 12px;
    color: var(--ink);
    font-family: "Saira", sans-serif;
    font-weight: 700;
    text-transform: uppercase;
    line-height: 1;
  }
  .brand-mark { width: 22px; height: 22px; background: var(--orange); flex: none; }
  .brand-name { font-size: 30px; letter-spacing: 1px; }
  .card-back .brand { right: 36px; bottom: 60px; }
  .card-front .brand { left: 130px; top: 70px; }

  .person {
    position: absolute;
    left: 34px;
    top: 226px;
    font-family: "Michroma", sans-serif;
    text-transform: uppercase;
    line-height: 1.1;
  }
  .person-name { color: var(--white); font-size: 17px; }
  .person-title { color: var(--orange); font-size: 15px; text-align: right; }

  .divider { position: absolute; left: 262px; top: 228px; width: 3px; height: 74px; background: var(--white); }

  .contacts {
    position: absolute;
    left: 282px;
    top: 226px;
    list-style: none;
    color: var(--white);
    font-size: 16px;
    letter-spacing: 1px;
  }
  .contacts li { display: flex; align-items: center; gap: 10px; height: 26px; }
  .icon { width: 17px; height: 15px; background: var(--orange); display: flex; align-items: center; justify-content: center; flex: none; }
  .icon svg { width: 11px; height: 11px; }
</style>
</head>
<body>

  <section class="card card-back" aria-label="Business card back">
    <div class="back-band"></div>
    <div class="back-rule"></div>
    <div class="brand">
      <span class="brand-mark"></span>
      <span class="brand-name">Valbrook Data Works</span>
    </div>
  </section>

  <section class="card card-front" aria-label="Business card front">
    <svg class="card-bg" viewBox="0 0 560 320" width="560" height="320" aria-hidden="true">
      <path d="M70,0 C88,170 240,246 392,232 C470,225 530,200 560,186 V0 Z" fill="var(--orange-deep)"/>
      <path d="M100,0 C118,150 250,228 388,223 C466,219 526,195 560,182 V0 Z" fill="var(--paper)"/>
    </svg>

    <div class="brand">
      <span class="brand-mark"></span>
      <span class="brand-name">Valbrook Data Works</span>
    </div>

    <div class="person">
      <p class="person-name">Marcus Ellery</p>
      <p class="person-title">Manager</p>
    </div>

    <div class="divider"></div>

    <ul class="contacts">
      <li>
        <span class="icon"><svg viewBox="0 0 12 12"><path d="M3 1 L5 3 L4 4.5 C5 6.5 5.5 7 7.5 8 L9 7 L11 9 L9.5 11 C5 10.5 1.5 7 1 2.5 Z" fill="var(--white)"/></svg></span>
        +1-555-014-2273
      </li>
      <li>
        <span class="icon"><svg viewBox="0 0 12 12"><rect x="1" y="2.5" width="10" height="7" fill="none" stroke="var(--white)" stroke-width="1.2"/><path d="M1 2.5 L6 7 L11 2.5" fill="none" stroke="var(--white)" stroke-width="1.2"/></svg></span>
        marcus@valbrookdata.com
      </li>
      <li>
        <span class="icon"><svg viewBox="0 0 12 12"><circle cx="6" cy="6" r="4.8" fill="none" stroke="var(--white)" stroke-width="1"/><path d="M1.2 6 H10.8 M6 1.2 C3.5 4 3.5 8 6 10.8 M6 1.2 C8.5 4 8.5 8 6 10.8" fill="none" stroke="var(--white)" stroke-width="0.9"/></svg></span>
        www.valbrookdata.com
      </li>
    </ul>
  </section>

</body>
</html>
```